This is a label for a new sake made in Japan imported into Aust

This will be a bottle label for a new sake imported into Australia. The hero of the label is the Trelu. We have joined the "O" meaning great in Japanese and used sake with "Z" to have Trelu with the play on words using Oz as in our slang for Aussie. A modern label with a Japanese take is key. This is a premium sake made in Japan for the Australian market.
The "Lark Hollow" up the top is the name of the company, we have yet to design a logo for the company.

Target Market(s)

Alcohol

Logo Text

Trelu

Font styles to use
Serif

Requirements
Must have
• easy to read, with a hint of Japanese origin
Should not have
• too busy

```html
<!DOCTYPE html>
<html lang="en">
<head>
<meta charset="utf-8">
<title>Trelu — Premium Japanese Sake Label</title>
<link href="https://fonts.googleapis.com/css2?family=Bebas+Neue&family=Patrick+Hand&family=Noto+Serif+JP:wght@500&display=swap" rel="stylesheet">
<style>
  :root {
    --label-black: #000000;
    --label-red: #ff0000;
    --label-white: #ffffff;
    --kanji-grey: #1b1b1b;
  }
  html, body {
    margin: 0;
    padding: 0;
    width: 958px;
    height: 1200px;
    overflow: hidden;
    background: var(--label-black);
  }
  .label {
    position: relative;
    width: 958px;
    height: 1200px;
    background: var(--label-black);
    overflow: hidden;
  }
  .company-bar {
    position: absolute;
    top: 48px;
    left: 0;
    width: 958px;
    height: 60px;
  }
  .lattice {
    position: absolute;
    top: 8px;
    height: 46px;
    width: 162px;
    background: linear-gradient(180deg, #b30000, #ff0000 50%, #b30000);
    opacity: 0.55;
  }
  .lattice--left { left: 0; }
  .lattice--right { right: 0; }
  .company-name {
    position: absolute;
    left: 176px;
    right: 176px;
    top: 0;
    margin: 0;
    text-align: center;
    font-family: "Bebas Neue", sans-serif;
    font-weight: 400;
    font-size: 72px;
    line-height: 60px;
    letter-spacing: 26px;
    padding-left: 26px;
    color: var(--label-red);
    white-space: nowrap;
  }
  .blossom {
    position: absolute;
    left: 291px;
    top: 281px;
    width: 372px;
    height: 185px;
    background: radial-gradient(ellipse at 50% 100%, #ff0000 0%, #a00000 55%, rgba(0,0,0,0) 80%);
    opacity: 0.8;
  }
  .rule {
    position: absolute;
    height: 13px;
    background: var(--label-red);
  }
  .rule--top { left: 60px; width: 841px; top: 473px; }
  .rule--bottom { left: 57px; width: 840px; top: 749px; }
  .brand {
    position: absolute;
    left: 60px;
    top: 500px;
    width: 840px;
    height: 230px;
  }
  .brand-dot {
    position: absolute;
    left: 2px;
    top: 17px;
    width: 206px;
    height: 200px;
    border-radius: 50%;
    background: var(--label-white);
  }
  .brand-name {
    position: absolute;
    left: 225px;
    top: -28px;
    margin: 0;
    font-family: "Patrick Hand", cursive;
    font-weight: 400;
    font-size: 250px;
    line-height: 1;
    color: var(--label-white);
    white-space: nowrap;
  }
  .stamen {
    position: absolute;
    left: 412px;
    top: 770px;
    width: 146px;
    height: 66px;
    background: radial-gradient(ellipse at 50% 20%, #d00000 0%, #700000 50%, rgba(0,0,0,0) 85%);
    opacity: 0.8;
  }
  .kanji {
    position: absolute;
    left: 0;
    top: 800px;
    width: 958px;
    margin: 0;
    text-align: center;
    font-family: "Noto Serif JP", serif;
    font-weight: 500;
    font-size: 330px;
    line-height: 1;
    letter-spacing: -8px;
    color: var(--kanji-grey);
    white-space: nowrap;
  }
  .tagline {
    position: absolute;
    left: 0;
    top: 900px;
    width: 958px;
    margin: 0;
    text-align: center;
    font-family: "Patrick Hand", cursive;
    font-weight: 400;
    font-size: 82px;
    line-height: 73px;
    letter-spacing: 8px;
    padding-left: 8px;
    box-sizing: border-box;
    color: var(--label-white);
  }
</style>
</head>
<body>
  <main class="label">
    <header class="company-bar">
      <div class="lattice lattice--left" role="img" aria-label="Red Japanese lattice border pattern"></div>
      <h2 class="company-name">LARK HOLLOW</h2>
      <div class="lattice lattice--right" role="img" aria-label="Red Japanese lattice border pattern"></div>
    </header>

    <p class="kanji" aria-hidden="true">日本酒</p>

    <div class="blossom" role="img" aria-label="Red stylised cherry blossom ornament"></div>
    <div class="rule rule--top"></div>

    <div class="brand">
      <span class="brand-dot"></span>
      <h1 class="brand-name">Trelu</h1>
    </div>

    <div class="rule rule--bottom"></div>
    <div class="stamen" role="img" aria-label="Small red blossom stamen ornament"></div>

    <p class="tagline">PREMIUM<br>JAPANESE<br>SAKE</p>
  </main>
</body>
</html>
```